Brightway Inc. Business Card Design

Brightway Inc. is in search of a great clean design for our business cards!

Looking to incorporate our full logo and watermark on side one (however, I am open to having the text and watermark separated within the design.)

On side two, I am looking to have contact information (Name, Position, Phone #, Email, Website (www.thebrightway.ca). Can have the logo and/or watermark as part of the design if applicable.

Please add tagline "Where Shine Counts" on either side 1 or 2. This tagline can be in a sans serif, serif or cursive font as long as it compliments overall design. Capitalization can be title or sentence case depending on how it fits within the design.

Get creative!! Looking for a clean, crisp, premium design! Looking for a glossy card finish with spot UV features when printed. Cards will also be printed with rounded corners. Standard dimensions (3.5 x 2).

Target Market(s)

B2B - primary clients are business owners or property management corporations. (residential jobs are few and far between)

Industry/Entity Type

Business

Contact Information for Business Card

- clean, crisp design
- double sided
- spot UV accents and glossy finish upon printing
- standard business card size (3.5 x 2) with rounded corners
- please see project description for requirements per side

Font styles to use
Sans Serif

Requirements
Must have
• - adequate bleeds with print ready files
• - cohesive design elements between side 1 & 2
• - spot UV elements (can be on both sides or just one, use your discretion)
• - colour pallet should match the logo file provided
• - incorporate tagline "where shine counts" (this tagline can be in a serif or sans serif font as long as it is complimentary to the overall design.
Nice to have
• - Premium elements with a clean design
Should not have
• - Please omit cartoon or whimsical like designs, think premium.
• - Colours should not stray from the pallet of the provided logo.

```html
<!DOCTYPE html>
<html lang="en">
<head>
<meta charset="utf-8">
<title>Brightway Inc. Business Card</title>
<link rel="stylesheet" href="https://fonts.googleapis.com/css2?family=Montserrat:wght@500;700;800&family=Arimo:wght@400&display=swap">
<style>
  :root {
    --backdrop: #453a33;
    --navy: #1c2a55;
    --teal: #13b3b8;
    --teal-deep: #1a9aa6;
    --ocean-edge: #1b4068;
    --wash-teal: #e4f6f6;
    --wash-grey: #eef0f3;
    --ink: #2a2f3a;
    --white: #ffffff;
  }
  * { box-sizing: border-box; margin: 0; padding: 0; }
  html, body { width: 1200px; height: 1200px; overflow: hidden; }
  body {
    background: var(--backdrop);
    position: relative;
    font-family: "Arimo", Arial, sans-serif;
  }
  .card {
    position: absolute;
    left: 180px;
    width: 840px;
    height: 480px;
    border-radius: 22px;
    overflow: hidden;
  }

  /* Side one: logo side */
  .card--brand {
    top: 90px;
    background: radial-gradient(ellipse at 50% 50%, #1fb0b5 0%, var(--teal-deep) 28%, #1a6f8d 60%, var(--ocean-edge) 100%);
    display: flex;
    flex-direction: column;
    align-items: center;
    justify-content: center;
  }
  .brand-lockup {
    display: flex;
    align-items: center;
    gap: 14px;
  }
  .brand-mark {
    width: 44px;
    height: 44px;
    background: var(--white);
  }
  .brand-name {
    font-family: "Montserrat", sans-serif;
    font-weight: 800;
    font-size: 52px;
    letter-spacing: 1px;
    color: var(--white);
  }
  .brand-tagline {
    margin-top: 8px;
    margin-left: 58px;
    font-family: "Arimo", sans-serif;
    font-size: 17px;
    letter-spacing: 9px;
    color: var(--white);
  }

  /* Side two: contact side */
  .card--contact {
    top: 630px;
    background: var(--white);
  }
  .contact-lockup {
    position: absolute;
    left: 52px;
    top: 56px;
    display: flex;
    align-items: center;
    gap: 12px;
  }
  .contact-lockup .brand-mark { background: var(--teal); width: 46px; height: 46px; }
  .contact-lockup .brand-name { color: var(--teal); font-size: 56px; }

  .watermark-area {
    position: absolute;
    left: 52px;
    top: 140px;
    width: 330px;
    height: 340px;
    background: linear-gradient(135deg, var(--wash-teal) 0%, var(--wash-teal) 55%, var(--wash-grey) 100%);
  }

  .divider {
    position: absolute;
    left: 448px;
    width: 1.5px;
    background: var(--navy);
  }
  .divider--top { top: 146px; height: 62px; }
  .divider--bottom { top: 238px; height: 80px; }

  .person {
    position: absolute;
    left: 476px;
    top: 150px;
  }
  .person-name {
    font-family: "Montserrat", sans-serif;
    font-weight: 700;
    font-size: 36px;
    letter-spacing: -0.5px;
    line-height: 1;
  }
  .person-name .given { color: var(--teal); }
  .person-name .family { color: var(--navy); }
  .person-role {
    margin-top: 8px;
    font-size: 19px;
    color: var(--ink);
  }

  .contact-list {
    position: absolute;
    left: 476px;
    top: 240px;
    list-style: none;
  }
  .contact-list li {
    display: flex;
    align-items: center;
    gap: 10px;
    font-size: 20px;
    color: var(--ink);
    line-height: 1.45;
  }
  .contact-list svg { width: 16px; height: 16px; flex: none; }

  .accent-band {
    position: absolute;
    left: 448px;
    right: 0;
    bottom: 0;
    height: 64px;
    background: var(--teal);
  }
</style>
</head>
<body>

<section class="card card--brand" aria-label="Card side one">
  <div class="brand-lockup">
    <span class="brand-mark"></span>
    <span class="brand-name">BRIGHTWAY INC.</span>
  </div>
  <p class="brand-tagline">Where Shine Counts</p>
</section>

<section class="card card--contact" aria-label="Card side two">
  <div class="contact-lockup">
    <span class="brand-mark"></span>
    <span class="brand-name">BRIGHTWAY INC.</span>
  </div>

  <div class="watermark-area" role="img" aria-label="Faint brand watermark decoration in pale teal and grey"></div>

  <span class="divider divider--top"></span>
  <span class="divider divider--bottom"></span>

  <div class="person">
    <h1 class="person-name"><span class="given">JOHN</span> <span class="family">DOE</span></h1>
    <p class="person-role">Director</p>
  </div>

  <ul class="contact-list">
    <li>
      <svg viewBox="0 0 16 16" aria-hidden="true"><path fill="#13b3b8" d="M3.5 1.5l2.5 0.2 1 3.2-1.6 1.2a9 9 0 0 0 4.5 4.5l1.2-1.6 3.2 1 0.2 2.5c-0.2 1-1 1.6-2 1.6C6.8 14.1 1.9 9.2 1.9 3.5c0-1 0.6-1.8 1.6-2z"/></svg>
      905-555-0147
    </li>
    <li>
      <svg viewBox="0 0 16 16" aria-hidden="true"><circle cx="8" cy="8" r="6.5" fill="none" stroke="#13b3b8" stroke-width="1.6"/><path d="M1.5 8h13M8 1.5c-2.4 2.8-2.4 10.2 0 13M8 1.5c2.4 2.8 2.4 10.2 0 13" fill="none" stroke="#13b3b8" stroke-width="1.2"/></svg>
      www.thebrightway.ca
    </li>
    <li>
      <svg viewBox="0 0 16 16" aria-hidden="true"><rect x="1" y="3" width="14" height="10" fill="#13b3b8"/></svg>
      info@brightwayservices.ca
    </li>
  </ul>

  <div class="accent-band"></div>
</section>

</body>
</html>
```